Prominent Law Firm Needs a New Stationary Design

We need new stationary design to go with our new logo and rustic offices.
Things we need on the letterhead:
logo (see attached file), would also like the Multi-Million Dollar Logo (attached) somewhere on the stationary,
3182 North Pellam Street
Tulsa, Oklahoma 74105
(918) 555-0142 Tel ★ (918) 555-0187 Fax
www.TFWLAW.example

We also need the names of the 4 partners:
Dennis W. Hollister
Walter E. Hollister
Kevin M. Abernathy
Brian D. Whitcombe

And the other staff:
Janet K. Bowden
Tendai K. Chikwanda
Howard Pimsley

Lorraine F. Tuttle, RN

Of Counsel:
Prescott D. Hollister

```html
<!DOCTYPE html>
<html lang="en">
<head>
<meta charset="utf-8">
<title>Hollister Hollister Abernathy — Business Card</title>
<link href="https://fonts.googleapis.com/css2?family=Didact+Gothic&display=swap" rel="stylesheet">
<style>
  :root {
    --backdrop: #e9e9eb;
    --card-dark: #1f1f1f;
    --card-light: #ffffff;
    --ink: #161616;
    --ink-soft: #555555;
    --ink-on-dark: #e4e4e4;
    --divider: #e2e2e2;
  }
  * { margin: 0; padding: 0; box-sizing: border-box; }
  html, body {
    width: 1200px; height: 1000px; overflow: hidden;
    background: var(--backdrop);
    font-family: "Didact Gothic", "Century Gothic", sans-serif;
    color: var(--ink);
  }
  .sheet {
    position: relative; width: 1200px; height: 1000px;
    display: flex; flex-direction: column; align-items: center; justify-content: center;
    gap: 60px;
  }
  .card {
    width: 700px; height: 400px;
    box-shadow: 0 10px 30px rgba(0,0,0,0.12);
  }
  .card--back {
    background: var(--card-dark);
    display: flex; align-items: center; justify-content: center;
  }
  .card--front {
    background: var(--card-light);
    display: grid; grid-template-columns: 1fr 1fr;
  }
  .brand {
    display: flex; flex-direction: column; align-items: center; gap: 16px;
    text-align: center;
  }
  .brand__dot {
    width: 18px; height: 18px; border-radius: 50%;
    background: currentColor;
  }
  .brand__name {
    font-size: 22px; letter-spacing: 3px; text-transform: uppercase; line-height: 1.5;
  }
  .card--back .brand { color: var(--ink-on-dark); }
  .card--back .brand__name { font-size: 30px; letter-spacing: 4px; }
  .card__logo-side {
    display: flex; align-items: center; justify-content: center;
    border-right: 1px solid var(--divider);
    color: var(--ink);
  }
  .card__info-side {
    padding: 70px 40px 0 44px;
  }
  .person__name {
    font-size: 22px; font-weight: 700; letter-spacing: 1px; text-transform: uppercase;
    -webkit-text-stroke: 0.5px var(--ink);
  }
  .person__role { font-size: 16px; color: var(--ink-soft); margin-top: 2px; }
  .contact { list-style: none; margin-top: 22px; font-size: 15px; line-height: 1.45; }
  .contact__label { font-weight: 700; -webkit-text-stroke: 0.4px var(--ink); }
  .address { font-style: normal; margin-top: 16px; font-size: 15px; line-height: 1.45; color: var(--ink-soft); }
</style>
</head>
<body>
  <main class="sheet">
    <section class="card card--back" aria-label="Card back">
      <div class="brand">
        <span class="brand__dot" aria-hidden="true"></span>
        <span class="brand__name">Hollister<br>Hollister<br>Abernathy</span>
      </div>
    </section>

    <section class="card card--front" aria-label="Card front">
      <div class="card__logo-side">
        <div class="brand">
          <span class="brand__dot" aria-hidden="true"></span>
          <span class="brand__name">Hollister<br>Hollister<br>Abernathy</span>
        </div>
      </div>
      <div class="card__info-side">
        <h1 class="person__name">Dennis W. Hollister</h1>
        <p class="person__role">Partner</p>
        <ul class="contact">
          <li><span class="contact__label">Tel:</span> (918) 555-0142</li>
          <li><span class="contact__label">Fax:</span> (918) 555-0187</li>
          <li><span class="contact__label">Email:</span> dennis@tfwlaw.example</li>
          <li><span class="contact__label">Web:</span> www.tfwlaw.example</li>
        </ul>
        <address class="address">3182 North Pellam Street<br>Tulsa, Oklahoma 74105</address>
      </div>
    </section>
  </main>
</body>
</html>
```